Doctor in Veterinary Medecine/ veterinarian

I am a vet and would like a buisness card which is simple yet elegant and professional.
My aim is to help as much animals as I can. My main field of expertise are dogs and cats. I would like the card to reflect a "family doctor" feeling.
It should not be the traditional picture of a paw or a dog but yet it should have a sign of a pet on it. I would like to have my name Lina Haddour as well as my profession D.V.M and my number.

Target Market(s)

Lebanese population who have pets

Industry/Entity Type

Doctor

Contact Information for Business Card

Should contain my profession " D.V.M", my full name "Lina Haddour" and my number "0096171552934"

Requirements
Must have
• A certain picture depicting my profession
Nice to have
• Some sort of picture related to pets and animals
Should not have
• A picture of a paw or a dog. I need something more creative

```html
<!DOCTYPE html>
<html lang="en">
<head>
<meta charset="utf-8">
<title>Warm Home Pets – Business Card</title>
<link rel="stylesheet" href="https://fonts.googleapis.com/css2?family=Baloo+2:wght@600&family=Open+Sans:wght@400;700&display=swap">
<style>
  :root {
    --backdrop: #eceded;
    --card: #ffffff;
    --green: #00a27f;
    --orange: #f08220;
    --ink: #2f2f2f;
    --illustration: #dfe6e3;
  }
  html, body {
    margin: 0;
    width: 1200px;
    height: 867px;
    overflow: hidden;
    background: var(--backdrop);
  }
  .business-card {
    position: absolute;
    left: 163px;
    top: 178px;
    width: 855px;
    height: 512px;
    background: var(--card);
    overflow: hidden;
    font-family: "Open Sans", Arial, sans-serif;
    color: var(--ink);
  }
  .top-swoosh {
    position: absolute;
    left: 0;
    top: 0;
    width: 855px;
    height: 120px;
  }
  .pet-illustration {
    position: absolute;
    left: 48px;
    top: 72px;
    width: 222px;
    height: 318px;
    border-radius: 40% 40% 30% 30%;
    background: radial-gradient(circle at 50% 35%, #f4f7f6 0%, var(--illustration) 70%);
  }
  .brand-name {
    position: absolute;
    left: 284px;
    top: 190px;
    margin: 0;
    font-family: "Baloo 2", "Open Sans", sans-serif;
    font-weight: 600;
    font-size: 52px;
    line-height: 1;
    color: var(--green);
    white-space: nowrap;
  }
  .tagline {
    position: absolute;
    left: 365px;
    top: 258px;
    margin: 0;
    font-size: 23px;
    letter-spacing: 5px;
    color: var(--ink);
  }
  .vet-name {
    position: absolute;
    left: 349px;
    top: 334px;
    margin: 0;
    font-size: 28px;
    font-weight: 700;
  }
  .vet-title {
    position: absolute;
    left: 384px;
    top: 372px;
    margin: 0;
    font-size: 26px;
    letter-spacing: 1px;
  }
  .contact-band {
    position: absolute;
    left: 0;
    bottom: 0;
    width: 100%;
    height: 87px;
    background: var(--green);
    display: flex;
    align-items: center;
    padding-left: 275px;
    box-sizing: border-box;
    color: #fff;
    font-size: 31px;
    font-weight: 700;
  }
  .phone-icon {
    width: 26px;
    height: 30px;
    margin-right: 8px;
  }
</style>
</head>
<body>
  <section class="business-card">
    <svg class="top-swoosh" viewBox="0 0 855 120" aria-hidden="true">
      <path d="M0,0 H560 C380,8 180,25 0,58 Z" fill="var(--orange)"/>
      <path d="M170,42 C420,0 700,15 855,82 V0 H500 C380,6 260,20 170,42 Z" fill="var(--green)"/>
      <path d="M170,42 C450,12 700,40 855,108 V86 C700,18 420,2 170,42 Z" fill="var(--orange)"/>
    </svg>

    <div class="pet-illustration" role="img" aria-label="Illustration of a cat wearing a stethoscope"></div>

    <h1 class="brand-name">Warm Home Pets</h1>
    <p class="tagline">VETERINARY CARE</p>

    <p class="vet-name">Lina Haddour</p>
    <p class="vet-title">D.V.M</p>

    <div class="contact-band">
      <svg class="phone-icon" viewBox="0 0 24 28" aria-hidden="true">
        <path d="M6,2 C4,2 2,5 2,9 C2,17 8,25 14,26 C17,26.5 19,25 20,23 L16.5,19 C15.5,19.8 14.5,20.5 13,20 C10,18 8,13 8.5,10 C9,8.8 10,8.2 11,8 L9.5,2.5 Z" fill="#fff"/>
      </svg>
      <span class="phone-number">0096171552934</span>
    </div>
  </section>
</body>
</html>
```